Powerpoint template for company, including logo placement, headers/footers with date, revision and page #s, matching fonts. Preferably white background with same color schemes as logo.

```html
<!DOCTYPE html>
<html lang="en">
<head>
<meta charset="utf-8">
<title>Slide Template</title>
<link href="https://fonts.googleapis.com/css2?family=PT+Sans:wght@400;700&display=swap" rel="stylesheet">
<style>
  :root {
    --brand-orange: #e5781a;
    --ink: #231f20;
    --paper: #ffffff;
  }
  html, body {
    margin: 0;
    padding: 0;
    overflow: hidden;
    background: var(--paper);
  }
  .slide {
    position: relative;
    width: 1200px;
    height: 849px;
    overflow: hidden;
    background: var(--paper);
    font-family: "PT Sans", sans-serif;
  }
  .top-band {
    position: absolute;
    left: 0; top: 0;
    width: 1200px; height: 56px;
    background: var(--brand-orange);
  }
  .logo-box {
    position: absolute;
    left: 934px; top: 28px;
    width: 154px; height: 147px;
    background: var(--paper);
    border: 2px solid var(--brand-orange);
    display: flex;
    align-items: center;
    justify-content: center;
  }
  .logo-name {
    font-size: 25px;
    font-weight: 700;
    color: var(--brand-orange);
    margin-top: 44px;
  }
  .company-name {
    position: absolute;
    left: 95px; top: 96px;
    margin: 0;
    font-size: 54px;
    font-weight: 700;
    color: var(--brand-orange);
    line-height: 1;
  }
  .points {
    position: absolute;
    left: 72px; top: 235px;
    margin: 0; padding: 0;
    list-style: none;
  }
  .point {
    display: flex;
    align-items: center;
    height: 78px;
    margin-bottom: 67px;
  }
  .point-marker {
    width: 40px; height: 78px;
    flex: none;
  }
  .point-text {
    margin-left: 36px;
    font-size: 58px;
    font-weight: 700;
    color: var(--brand-orange);
    line-height: 1;
  }
  .footer-meta {
    position: absolute;
    right: 213px; top: 784px;
    font-size: 17px;
    font-weight: 700;
    color: var(--ink);
    letter-spacing: 0.3px;
  }
  .page-number {
    position: absolute;
    left: 1003px; top: 762px;
    width: 59px; height: 58px;
    background: var(--ink);
    color: var(--paper);
    font-size: 32px;
    font-weight: 700;
    display: flex;
    align-items: center;
    justify-content: center;
  }
  .bottom-band {
    position: absolute;
    left: 0; top: 800px;
    width: 1200px; height: 49px;
  }
</style>
</head>
<body>
  <div class="slide">
    <div class="top-band"></div>

    <div class="logo-box">
      <span class="logo-name">Your Logo</span>
    </div>

    <h1 class="company-name">Your Company Name</h1>

    <ul class="points">
      <li class="point">
        <svg class="point-marker" viewBox="0 0 40 78"><polygon points="0,0 40,39 0,78" fill="#231f20"/></svg>
        <span class="point-text">Points 1</span>
      </li>
      <li class="point">
        <svg class="point-marker" viewBox="0 0 40 78"><polygon points="0,0 40,39 0,78" fill="#231f20"/></svg>
        <span class="point-text">Points 1</span>
      </li>
      <li class="point">
        <svg class="point-marker" viewBox="0 0 40 78"><polygon points="0,0 40,39 0,78" fill="#231f20"/></svg>
        <span class="point-text">Points 1</span>
      </li>
      <li class="point">
        <svg class="point-marker" viewBox="0 0 40 78"><polygon points="0,0 40,39 0,78" fill="#231f20"/></svg>
        <span class="point-text">Points 1</span>
      </li>
    </ul>

    <div class="footer-meta">11th Decebmer 2014 | Revison</div>
    <div class="page-number">1</div>

    <svg class="bottom-band" viewBox="0 0 1200 49" preserveAspectRatio="none">
      <path d="M0,7 C250,14 500,26 760,38 L760,49 L0,49 Z" fill="#231f20"/>
      <path d="M0,38 L700,38 C900,30 1080,18 1200,6 L1200,49 L0,49 Z" fill="#e5781a"/>
    </svg>
  </div>
</body>
</html>
```